Webpage Needed for Bright Harbor Wiring Electrical and Security

We need a web design for our company showing people we arent just a small business. We want to look big so people can trust us. I would like information from my business cards on the page. example, we do all house rennovations, construction, commercial, 24 hour emergency service, new installations, repairs, maintenance, home theatre and so on...

I would also like images from my facebook on the page and linked. facebook.com/brightharborwiring

Target Market(s)

builders, residents,

Industry/Entity Type

Business

Number of Pages Required

1 page

Font styles to use
Other font styles liked:
• Juice bold

Requirements
Must have
• colours the same as the logo. background must be white. also the font must be Juice Bold which is the font of the logo
Should not have
• black as the background

```html
<!DOCTYPE html>
<html lang="en">
<head>
<meta charset="utf-8">
<title>Bright Harbor Wiring – Electrical and Security</title>
<link rel="stylesheet" href="https://fonts.googleapis.com/css2?family=Oswald:wght@400;500&family=Open+Sans:wght@400;600&family=Roboto:wght@300;400&display=swap">
<style>
:root{
  --red:#e0322a;
  --orange:#e8672c;
  --ink:#333333;
  --muted:#555555;
  --soft-bg:#f2f2f2;
  --white:#ffffff;
  --footer:#262626;
  --footer-line:#3a3a3a;
  --hero-dark:#2a2a2a;
}
*{margin:0;padding:0;box-sizing:border-box}
html,body{width:1200px;height:2244px;overflow:hidden;background:var(--white)}
body{font-family:"Open Sans",Arial,sans-serif;color:var(--ink);position:relative}
.section{position:absolute;left:0;width:1200px}
.abs{position:absolute}

/* Header */
.site-header{top:0;height:122px;background:var(--white)}
.brand{left:98px;top:24px;width:150px;font-family:"Oswald",sans-serif;font-weight:500;font-size:27px;line-height:28px;color:var(--orange)}
.main-nav{left:380px;top:52px;display:flex;font-family:"Roboto",sans-serif;font-size:15px;color:var(--ink)}
.main-nav a{color:inherit;text-decoration:none;padding:0 30px;border-left:1px solid #e6e6e6;line-height:28px}
.main-nav a:first-child{border-left:none}
.emergency{left:884px;top:46px}
.emergency-label{left:940px;top:38px;font-family:"Oswald",sans-serif;font-size:15px;color:#777;white-space:nowrap}
.emergency-number{left:940px;top:64px;font-family:"Open Sans",sans-serif;font-weight:600;font-size:19px;color:var(--orange);letter-spacing:1px;white-space:nowrap}

/* Hero */
.hero{top:122px;height:503px;background:linear-gradient(90deg,#8f9296 0%,#5b5d60 30%,#3a3a3a 55%,#2c2c2c 100%)}
.hero-title{right:97px;top:140px;text-align:right;font-family:"Oswald",sans-serif;font-weight:500;font-size:44px;line-height:58px;color:var(--white)}
.hero-text{right:97px;top:262px;width:360px;text-align:right;font-family:"Oswald",sans-serif;font-size:15px;line-height:28px;color:var(--white)}
.slider-arrow{top:260px}
.slider-dots{left:818px;top:456px}

/* Welcome */
.welcome{top:625px;height:208px;background:var(--soft-bg);text-align:center}
.welcome h1{position:absolute;top:40px;width:1200px;font-family:"Oswald",sans-serif;font-weight:500;font-size:32px;color:var(--ink)}
.welcome h1 span{color:var(--red)}
.welcome p{position:absolute;left:170px;top:95px;width:860px;font-size:11px;line-height:20px;color:var(--muted)}

/* Services */
.services{top:833px;height:404px;background:var(--white)}
.services h2{left:122px;top:44px;font-family:"Roboto",sans-serif;font-weight:300;font-size:31px;color:var(--ink)}
.services-intro{left:124px;top:98px;width:500px;font-size:12px;line-height:21px;color:var(--muted)}
.service-list{left:124px;top:158px;list-style:none;font-size:12.5px;color:var(--ink)}
.service-list li{height:28.5px;display:flex;align-items:center;gap:12px}
.tablet{left:698px;top:70px;width:368px;height:280px;background:#111;border-radius:18px;border:3px solid #3a3a3a}
.tablet-screen{position:absolute;left:30px;top:26px;width:298px;height:222px;background:linear-gradient(135deg,#6a7078 0%,#9aa6b4 45%,#c7cdd4 70%,#5e6670 100%)}

/* Why us */
.why{top:1237px;height:500px;background:var(--soft-bg)}
.why h2{left:97px;top:36px;font-family:"Oswald",sans-serif;font-weight:500;font-size:34px;color:var(--red)}
.why-sub{left:97px;top:86px;font-family:"Roboto",sans-serif;font-size:19px;color:#444}
.feature{top:142px;width:318px}
.feature-photo{width:318px;height:197px;border:4px solid var(--white);box-shadow:0 0 0 1px #ddd}
.feature h3{margin-top:18px;font-family:"Open Sans",sans-serif;font-weight:400;font-size:20px;color:var(--ink)}
.feature p{margin-top:8px;font-size:11.5px;line-height:20px;color:var(--muted)}

/* News */
.news{top:1737px;height:329px;background:var(--white)}
.news h2{left:97px;top:50px;font-family:"Oswald",sans-serif;font-weight:400;font-size:21px;color:var(--ink)}
.news-item{top:102px;width:480px;height:170px}
.news-photo{position:absolute;left:0;top:0;width:188px;height:164px}
.news-body{position:absolute;left:214px;top:0;width:270px}
.news-body h3{font-family:"Open Sans",sans-serif;font-weight:400;font-size:16px;color:var(--ink)}
.news-date{margin-top:14px;font-size:12px;color:var(--orange)}
.news-body p{margin-top:10px;font-size:11px;line-height:19.5px;color:var(--muted)}
.read-more{position:absolute;left:0;top:148px;font-size:13px;color:var(--ink);text-decoration:none}

/* Footer */
.site-footer{top:2066px;height:178px;background:var(--footer)}
.cta-label{left:99px;top:30px;font-family:"Oswald",sans-serif;font-size:21px;color:var(--white)}
.cta-phone{left:99px;top:64px;font-size:15px;color:var(--red)}
.address{left:497px;top:34px;font-size:13.5px;line-height:28px;color:#ddd}
.social{left:906px;top:36px}
.copyright{top:134px;width:1200px;text-align:center;font-size:11px;color:#999}
</style>
</head>
<body>

<header class="section site-header">
  <div class="abs brand">Bright Harbor Wiring</div>
  <nav class="abs main-nav">
    <a href="#">Home</a><a href="#">About Us</a><a href="#">Our Services</a><a href="#">Contact Us</a>
  </nav>
  <svg class="abs emergency" width="42" height="42" viewBox="0 0 42 42">
    <circle cx="21" cy="21" r="19" fill="none" stroke="var(--orange)" stroke-width="1.6"/>
    <path d="M15 13c1-1 2-1 3 0l2 3c.5 1 .3 1.8-.5 2.4l-1 .8c.8 2 2.3 3.6 4.3 4.4l.8-1c.6-.8 1.5-1 2.4-.5l3 2c1 .7 1 1.8 0 2.8l-1.3 1.3c-1 1-2.6 1.2-4 .5-4.4-2.2-7.6-5.4-9.7-9.8-.7-1.4-.4-3 .6-4z" fill="var(--orange)"/>
  </svg>
  <div class="abs emergency-label">24 Hour Emergency Service</div>
  <div class="abs emergency-number">907 - 555 - 0142</div>
</header>

<section class="section hero">
  <div class="abs" style="left:0;top:0;width:1200px;height:503px" role="img" aria-label="Photo of the company service truck parked in a warehouse"></div>
  <h1 class="abs hero-title">Bright Harbor Wiring<br>Electrical and Security</h1>
  <p class="abs hero-text">Lorem ipsum dolor sit amet, consectetur adipiscing elit, sed do eiusmod tempor incididunt ut labore et dolore magna aliqua. Ut enim ad minim veniam</p>
  <svg class="abs slider-arrow" style="left:34px" width="36" height="36" viewBox="0 0 36 36"><circle cx="18" cy="18" r="17" fill="#1b1b1b"/><path d="M21 11l-7 7 7 7" fill="none" stroke="#fff" stroke-width="2.5"/></svg>
  <svg class="abs slider-arrow" style="left:1124px" width="36" height="36" viewBox="0 0 36 36"><circle cx="18" cy="18" r="17" fill="#1b1b1b"/><path d="M15 11l7 7-7 7" fill="none" stroke="#fff" stroke-width="2.5"/></svg>
  <svg class="abs slider-dots" width="100" height="10" viewBox="0 0 100 10"><circle cx="5" cy="5" r="3.5" fill="#111"/><circle cx="35" cy="5" r="3.5" fill="#111"/><circle cx="93" cy="5" r="3.5" fill="#111"/></svg>
</section>

<section class="section welcome">
  <h1>Welcome To <span>Bright Harbor Wiring</span></h1>
  <p>Lorem ipsum dolor sit amet, consectetur adipiscing elit, sed do eiusmod tempor incididunt ut labore et dolore magna aliqua. Ut enim ad minim veniam, quis nostrud exercitation ullamco laboris nisi ut aliquip ex ea commodo consequat. Duis aute irure dolor in reprehenderit in voluptate velit esse cillum dolore eu fugiat nulla pariatur. Excepteur sint occaecat cupidatat non proident, sunt in culpa qui officia deserunt mollit anim id est laborum</p>
</section>

<section class="section services">
  <h2 class="abs">What we Do?</h2>
  <p class="abs services-intro">Sed ut perspiciatis unde omnis iste natus error sit voluptatem accusantium doloremque laudantium, totam rem aperiam, eaque ipsa quae ab illo inventore</p>
  <ul class="abs service-list">
    <li><svg width="12" height="10" viewBox="0 0 12 10"><path d="M1 5l3.5 3.5L11 1" fill="none" stroke="var(--red)" stroke-width="2"/></svg>House Renovations,</li>
    <li><svg width="12" height="10" viewBox="0 0 12 10"><path d="M1 5l3.5 3.5L11 1" fill="none" stroke="var(--red)" stroke-width="2"/></svg>Construction, Commercial,</li>
    <li><svg width="12" height="10" viewBox="0 0 12 10"><path d="M1 5l3.5 3.5L11 1" fill="none" stroke="var(--red)" stroke-width="2"/></svg>24 Hour Emergency Service,</li>
    <li><svg width="12" height="10" viewBox="0 0 12 10"><path d="M1 5l3.5 3.5L11 1" fill="none" stroke="var(--red)" stroke-width="2"/></svg>New Installations, Repairs,</li>
    <li><svg width="12" height="10" viewBox="0 0 12 10"><path d="M1 5l3.5 3.5L11 1" fill="none" stroke="var(--red)" stroke-width="2"/></svg>Maintenance,</li>
    <li><svg width="12" height="10" viewBox="0 0 12 10"><path d="M1 5l3.5 3.5L11 1" fill="none" stroke="var(--red)" stroke-width="2"/></svg>Home Theatre</li>
  </ul>
  <div class="abs tablet">
    <div class="tablet-screen" role="img" aria-label="Photo of an electrician fitting a ceiling light"></div>
  </div>
</section>

<section class="section why">
  <h2 class="abs">WHY PEOPLE CHOOSE US?</h2>
  <p class="abs why-sub">Donec sodales sagittis magna sed consequat leo eget bibendum sodales</p>
  <article class="abs feature" style="left:97px">
    <div class="feature-photo" role="img" aria-label="Photo of a renovated office with warm lighting" style="background:linear-gradient(135deg,#3a2a1a 0%,#b07a3a 45%,#e8b860 60%,#4a3320 100%)"></div>
    <h3>House Renovations</h3>
    <p>Sed ut perspiciatis unde omnis iste natus error sit volupta-tem accusantium doloremque laudantium, totam rem aperiam, eaque ipsa quae ab...</p>
  </article>
  <article class="abs feature" style="left:440px">
    <div class="feature-photo" role="img" aria-label="Photo of a cordless drill fixing a wall panel" style="background:linear-gradient(135deg,#c9ccd0 0%,#9fb0c4 45%,#6c7c8e 70%,#d8dadc 100%)"></div>
    <h3>New Installations</h3>
    <p>Sed ut perspiciatis unde omnis iste natus error sit volupta-tem accusantium doloremque laudantium, totam rem aperiam, eaque ipsa quae ab...</p>
  </article>
  <article class="abs feature" style="left:783px">
    <div class="feature-photo" role="img" aria-label="Photo of a home theatre room with projector screen" style="background:linear-gradient(135deg,#2a2220 0%,#4a3a34 45%,#6a5248 60%,#1e1816 100%)"></div>
    <h3>Home Theatre</h3>
    <p>Sed ut perspiciatis unde omnis iste natus error sit volupta-tem accusantium doloremque laudantium, totam rem aperiam, eaque ipsa quae ab...</p>
  </article>
</section>

<section class="section news">
  <h2 class="abs">LATEST NEWS</h2>
  <article class="abs news-item" style="left:97px">
    <div class="news-photo" role="img" aria-label="Photo of an electrician working on a ceiling fitting" style="background:linear-gradient(135deg,#1e1e1e 0%,#4a4a44 50%,#c8c860 80%,#2a2a2a 100%)"></div>
    <div class="news-body">
      <h3>Nulla at diam ornare, aliquam urna</h3>
      <div class="news-date">MAY 25, 2015</div>
      <p>Nulla at diam ornare, aliquam urna vel, commodo urna. Nam id risus a est luctus consectetur quis eget libero. Suspendisse potenti. Pellentesque habitant morbi tristique senectus</p>
      <a class="read-more" href="#">Read More +</a>
    </div>
  </article>
  <article class="abs news-item" style="left:630px">
    <div class="news-photo" role="img" aria-label="Photo of a worker outside a stone building" style="background:linear-gradient(160deg,#5e7a3e 0%,#a8a49a 45%,#3a3a36 75%,#6a6a64 100%)"></div>
    <div class="news-body">
      <h3>Nulla at diam ornare, aliquam urna</h3>
      <div class="news-date">MAY 25, 2015</div>
      <p>Nulla at diam ornare, aliquam urna vel, commodo urna. Nam id risus a est luctus consectetur quis eget libero. Suspendisse potenti. Pellentesque habitant morbi tristique senectus</p>
      <a class="read-more" href="#">Read More +</a>
    </div>
  </article>
</section>

<footer class="section site-footer">
  <div class="abs cta-label">For a Free Consultation Call :</div>
  <div class="abs cta-phone">+1 9028 555 019</div>
  <address class="abs address" style="font-style:normal">9870 St Bright Harbor Place,<br>Glasgow, DC 45 Fr 45.</address>
  <svg class="abs social" width="196" height="36" viewBox="0 0 196 36">
    <circle cx="18" cy="18" r="17" fill="#444"/>
    <circle cx="58" cy="18" r="17" fill="#444"/>
    <circle cx="98" cy="18" r="17" fill="#444"/>
    <circle cx="138" cy="18" r="17" fill="#444"/>
    <circle cx="178" cy="18" r="17" fill="#444"/>
  </svg>
  <div class="abs copyright">© 2015 Bright Harbor Wiring - All Rights Reserved</div>
</footer>

</body>
</html>
```